Corvane Stationery Design

We need design for our stationary, including:
1) Letterhead
- A4/Letter size in landscape and portrait letterhead
- The letterhead must be in a word file, and the address should be editable using the Felixti or Perpetua Titling TTF
- The output file should be in .docx and in .ai.
2) Business card
- The business card will be printed in white paper and single face only, so there should be nothing on the reverse side.
3) Envelope (sizes A4, Letter, and small document)
Please refer to the picture showing some samples of stationary with designs that would fulfill our wish.
We're including the logo in .AI.
Thanks
Target Market(s)
High end investors
Industry/Entity Type
Landscape
Look and feel

```html
<!DOCTYPE html>
<html lang="en">
<head>
<meta charset="utf-8">
<title>Corvane Capital Partners — Letterhead</title>
<link rel="stylesheet" href="https://fonts.googleapis.com/css2?family=Cinzel:wght@400;700&display=swap">
<style>
  :root {
    --paper: #ffffff;
    --ink: #2a2a2a;
    --teal: #1a98b6;
    --footer-text: #ffffff;
  }
  html, body {
    margin: 0;
    padding: 0;
    overflow: hidden;
    background: var(--paper);
  }
  .letterhead {
    position: relative;
    width: 849px;
    height: 1200px;
    background: var(--paper);
    overflow: hidden;
  }
  .brand {
    position: absolute;
    top: 46px;
    right: 48px;
    width: 280px;
    text-align: center;
    font-family: "Cinzel", serif;
    font-weight: 400;
    color: var(--ink);
  }
  .brand-name {
    display: block;
    font-size: 44px;
    line-height: 48px;
    letter-spacing: 3px;
  }
  .brand-descriptor {
    display: block;
    margin-top: 6px;
    font-size: 15px;
    letter-spacing: 6px;
  }
  .footer-band {
    position: absolute;
    left: 0;
    top: 0;
    width: 849px;
    height: 1200px;
  }
  .footer-contact {
    position: absolute;
    left: 0;
    width: 816px;
    top: 1130px;
    margin: 0;
    text-align: center;
    font-family: "Cinzel", serif;
    font-weight: 700;
    font-size: 17px;
    line-height: 25px;
    color: var(--footer-text);
  }
</style>
</head>
<body>
  <main class="letterhead">
    <header class="brand">
      <span class="brand-name">CORVANE</span>
      <span class="brand-descriptor">CAPITAL PARTNERS</span>
    </header>

    <svg class="footer-band" viewBox="0 0 849 1200" aria-hidden="true">
      <path d="M0 1131 Q 425 1061 849 1136 L849 1200 L0 1200 Z" fill="var(--teal)"/>
    </svg>

    <footer>
      <p class="footer-contact">THIS IS OUR ADDRESS, WRITE TO US HERE, CALL US HERE<br>EMAIL US HERE, VISIT OUR WEBSITE</p>
    </footer>
  </main>
</body>
</html>
```